Electrical Safety Inspection for High End Customers

Flyer designed to advertise a 50 point electrical safety check service available from a recent start up electrician's firm in Auckland, New Zealand. I am a registered electrical inspector with 16 years experience.
Targeting high end customers, so I want the flyer to have a premium feel to it (glossy black background, etc). The final design should communicate peace of mind. The price will be $60 incl. GST
The checks included should be 1) Mains Cable 2)Mains entry point 3)Switchboard 4)Circuit protection correctly rated 5)Circuit protection operational 6)The main earthing system 7)Safety systems 8)Light fittings 9)Socket outlets 10)Deterioration of fittings 11)Deterioration of cabling 12)Compliance with current regulations
I have included a copy of the test sheet for reference. I have also included my logo and the qualified wiremen's guild of Ostravel, both of which must be present.
Target Market(s)
High end home owners
Industry/Entity Type
Electrician
Colors
Designer to choose colors to be used in the design.
Look and feel

```html
<!DOCTYPE html>
<html lang="en">
<head>
<meta charset="utf-8">
<title>Kestrel Line Electrical – 50 Point Electrical Safety Check</title>
<link href="https://fonts.googleapis.com/css2?family=Exo+2:wght@400;500;700;800&display=swap" rel="stylesheet">
<style>
  :root{
    --blue:#1479c8;
    --blue-deep:#0d5fa6;
    --ink:#111214;
    --ink-soft:#2a2c30;
    --white:#ffffff;
    --text:#1b1b1b;
    --page:#e9eaec;
    --photo-a:#c9a77a;
    --photo-b:#7b5a3a;
  }
  *{margin:0;padding:0;box-sizing:border-box}
  html,body{width:1200px;height:791px;overflow:hidden;background:var(--page)}
  body{position:relative;font-family:"Exo 2",sans-serif}
  .flyer{
    position:absolute;left:332px;top:16px;width:596px;height:843px;
    transform:scale(0.9);transform-origin:0 0;
    background:var(--white);overflow:hidden;
    box-shadow:0 4px 18px rgba(0,0,0,.18);
  }
  .abs{position:absolute}
  .hero-art{left:0;top:0;width:596px;height:310px}
  .brand{left:28px;top:40px;display:flex;align-items:center;gap:12px}
  .brand-dot{width:46px;height:46px;border-radius:50%;background:var(--ink)}
  .brand-name{font-weight:800;font-size:27px;color:var(--ink);letter-spacing:.5px;line-height:1}
  .headline{left:18px;top:150px;color:var(--white)}
  .headline .big{font-weight:800;font-size:46px;letter-spacing:1px;line-height:1}
  .headline .sub{font-weight:400;font-size:33px;line-height:38px;margin-top:2px}
  .price{left:380px;top:261px;width:180px;text-align:center;color:var(--white);font-size:22px;font-weight:500}
  .sectors{left:0;top:310px;width:596px;height:130px;
    background:linear-gradient(180deg,var(--ink) 0%,var(--ink-soft) 55%,var(--ink) 100%)}
  .sector{position:absolute;top:0;height:130px;width:200px;text-align:center;color:var(--white);font-size:14px}
  .sector svg{margin-top:32px}
  .sector span{position:absolute;left:0;right:0;top:89px}
  .divider{position:absolute;top:14px;width:1px;height:104px;background:#4a4d52}
  .divider.blue{background:var(--blue)}
  .tagline{left:0;top:456px;width:596px;text-align:center;font-size:24px;color:var(--text)}
  .banner{left:0;top:492px;width:596px;height:24px}
  .banner-text{left:0;top:493px;width:596px;text-align:center;color:var(--white);font-size:17px;font-weight:500;letter-spacing:.3px}
  .checks{left:36px;top:530px;width:560px;display:grid;grid-template-columns:274px 286px;row-gap:8px;list-style:none}
  .checks li{display:flex;align-items:center;gap:6px;height:28px;font-size:15px;color:var(--text)}
  .checks svg{flex:none}
  .badges{left:428px;top:745px;display:flex;align-items:center;gap:10px}
  .badge-round{width:40px;height:40px;border-radius:50%;background:var(--blue-deep);border:3px solid #9cc6ea}
  .badge-member{width:94px;height:34px;background:#f1f4f8;border-bottom:2px solid var(--blue)}
  .footer-art{left:0;top:768px;width:596px;height:75px}
  .contact{left:24px;top:786px;color:var(--white);font-size:16px;letter-spacing:1.3px;line-height:25px}
  .contact div{display:flex;align-items:center;gap:7px}
  .phone{left:368px;top:801px;color:var(--white);font-size:18px;font-weight:700;letter-spacing:.8px;display:flex;align-items:center;gap:8px}
</style>
</head>
<body>
<main class="flyer">
  <svg class="abs hero-art" viewBox="0 0 596 310">
    <defs>
      <linearGradient id="photoTone" x1="0" y1="0" x2="1" y2="1">
        <stop offset="0" stop-color="#e9dccb"/>
        <stop offset=".5" stop-color="var(--photo-a)"/>
        <stop offset="1" stop-color="var(--photo-b)"/>
      </linearGradient>
    </defs>
    <polygon points="370,0 596,0 596,310 330,310 262,160" fill="url(#photoTone)" role="img" aria-label="Photograph of an electrician in a tool belt holding a cordless drill"/>
    <polygon points="0,124 237,124 355,310 0,310" fill="var(--blue)"/>
    <polygon points="352,256 592,256 566,296 326,296" fill="var(--ink)"/>
  </svg>

  <div class="abs brand"><span class="brand-dot"></span><span class="brand-name">KESTREL LINE ELECTRICAL</span></div>

  <div class="abs headline">
    <div class="big">50 POINT</div>
    <div class="sub">electrical safety<br>check service</div>
  </div>
  <div class="abs price">$60 incl. GST</div>

  <section class="abs sectors">
    <div class="sector" style="left:12px">
      <svg width="54" height="46" viewBox="0 0 54 46" fill="var(--blue)"><rect x="2" y="26" width="50" height="18"/><polygon points="2,26 14,18 14,26 26,18 26,26 38,18 38,26"/><rect x="40" y="6" width="5" height="20"/><rect x="30" y="10" width="5" height="16"/></svg>
      <span>INDUSTRIAL</span>
    </div>
    <div class="divider" style="left:200px"></div>
    <div class="sector" style="left:198px">
      <svg width="48" height="46" viewBox="0 0 48 46" fill="none" stroke="var(--blue)" stroke-width="4"><rect x="4" y="4" width="40" height="38"/><line x1="4" y1="14" x2="44" y2="14"/><rect x="12" y="22" width="8" height="8"/><rect x="28" y="22" width="8" height="8"/></svg>
      <span>DOMESTIC</span>
    </div>
    <div class="divider blue" style="left:405px"></div>
    <div class="sector" style="left:396px">
      <svg width="52" height="46" viewBox="0 0 52 46" fill="var(--blue)"><polygon points="4,10 30,4 30,44 4,44"/><rect x="30" y="16" width="16" height="28"/><g fill="var(--ink)"><rect x="9" y="16" width="5" height="5"/><rect x="19" y="16" width="5" height="5"/><rect x="9" y="27" width="5" height="5"/><rect x="19" y="27" width="5" height="5"/></g></svg>
      <span>COMMERCIAL</span>
    </div>
  </section>

  <h2 class="abs tagline" style="font-weight:400">Leaders in Electrical Design and Installation</h2>
  <svg class="abs banner" viewBox="0 0 596 24"><polygon points="130,0 474,0 462,24 118,24" fill="var(--blue)"/></svg>
  <div class="abs banner-text">SOME OF THE CHECK SERVICES</div>

  <ul class="abs checks">
    <li><svg width="36" height="34" viewBox="0 0 36 34"><polygon points="9,2 27,2 35,17 27,32 9,32 1,17" fill="var(--ink)" stroke="var(--blue)" stroke-width="2"/><path d="M11 11l14 12M25 11L11 23" stroke="var(--blue)" stroke-width="3"/></svg>Mains Cable</li>
    <li><svg width="36" height="34" viewBox="0 0 36 34"><polygon points="9,2 27,2 35,17 27,32 9,32 1,17" fill="var(--ink)" stroke="var(--blue)" stroke-width="2"/><path d="M18 9l-3 16h7" stroke="var(--blue)" stroke-width="3" fill="none"/></svg>Safety systems</li>
    <li><svg width="36" height="34" viewBox="0 0 36 34"><polygon points="9,2 27,2 35,17 27,32 9,32 1,17" fill="var(--ink)" stroke="var(--blue)" stroke-width="2"/><rect x="12" y="10" width="12" height="14" fill="var(--blue)"/></svg>Mains entry point</li>
    <li><svg width="36" height="34" viewBox="0 0 36 34"><polygon points="9,2 27,2 35,17 27,32 9,32 1,17" fill="var(--ink)" stroke="var(--blue)" stroke-width="2"/><circle cx="18" cy="15" r="6" fill="none" stroke="var(--blue)" stroke-width="2.5"/><rect x="15" y="21" width="6" height="4" fill="var(--blue)"/></svg>Light fittings</li>
    <li><svg width="36" height="34" viewBox="0 0 36 34"><polygon points="9,2 27,2 35,17 27,32 9,32 1,17" fill="var(--ink)" stroke="var(--blue)" stroke-width="2"/><rect x="13" y="10" width="10" height="14" fill="none" stroke="var(--blue)" stroke-width="2.5"/></svg>Switchboard</li>
    <li><svg width="36" height="34" viewBox="0 0 36 34"><polygon points="9,2 27,2 35,17 27,32 9,32 1,17" fill="var(--ink)" stroke="var(--blue)" stroke-width="2"/><rect x="11" y="10" width="14" height="14" rx="2" fill="none" stroke="var(--blue)" stroke-width="2.5"/><circle cx="18" cy="17" r="2.5" fill="var(--blue)"/></svg>Socket outlets</li>
    <li><svg width="36" height="34" viewBox="0 0 36 34"><polygon points="9,2 27,2 35,17 27,32 9,32 1,17" fill="var(--ink)" stroke="var(--blue)" stroke-width="2"/><rect x="10" y="11" width="16" height="12" fill="var(--blue)"/></svg>Circuit protection correctly rated</li>
    <li><svg width="36" height="34" viewBox="0 0 36 34"><polygon points="9,2 27,2 35,17 27,32 9,32 1,17" fill="var(--ink)" stroke="var(--blue)" stroke-width="2"/><path d="M22 9h-6v16h6" stroke="var(--blue)" stroke-width="3" fill="none"/></svg>Deterioration of fittings</li>
    <li><svg width="36" height="34" viewBox="0 0 36 34"><polygon points="9,2 27,2 35,17 27,32 9,32 1,17" fill="var(--ink)" stroke="var(--blue)" stroke-width="2"/><circle cx="18" cy="14" r="4" fill="var(--blue)"/><rect x="12" y="19" width="12" height="6" fill="var(--blue)"/></svg>Circuit protection operational</li>
    <li><svg width="36" height="34" viewBox="0 0 36 34"><polygon points="9,2 27,2 35,17 27,32 9,32 1,17" fill="var(--ink)" stroke="var(--blue)" stroke-width="2"/><path d="M11 23l9-12 5 5" stroke="var(--blue)" stroke-width="3" fill="none"/></svg>Deterioration of cabling</li>
    <li><svg width="36" height="34" viewBox="0 0 36 34"><polygon points="9,2 27,2 35,17 27,32 9,32 1,17" fill="var(--ink)" stroke="var(--blue)" stroke-width="2"/><polygon points="18,9 26,24 10,24" fill="none" stroke="var(--blue)" stroke-width="2.5"/></svg>The main earthing system</li>
    <li><svg width="36" height="34" viewBox="0 0 36 34"><polygon points="9,2 27,2 35,17 27,32 9,32 1,17" fill="var(--ink)" stroke="var(--blue)" stroke-width="2"/><rect x="12" y="9" width="12" height="16" fill="none" stroke="var(--blue)" stroke-width="2.5"/><path d="M15 14h6M15 18h6" stroke="var(--blue)" stroke-width="2"/></svg>Compliance with current regulations</li>
  </ul>

  <div class="abs badges" aria-label="Experience badge and qualified wiremen's guild of Ostravel membership">
    <span class="badge-round"></span><span class="badge-member"></span>
  </div>

  <svg class="abs footer-art" viewBox="0 0 596 75">
    <polygon points="0,0 304,0 380,75 0,75" fill="var(--ink)"/>
    <polygon points="346,22 590,22 556,62 326,62" fill="var(--blue)"/>
  </svg>

  <div class="abs contact">
    <div><svg width="14" height="14" viewBox="0 0 14 14"><circle cx="7" cy="7" r="6" fill="var(--blue)"/><rect x="3.5" y="4.5" width="7" height="5" fill="none" stroke="var(--ink)" stroke-width="1.2"/></svg>info@kestrellineelectrical.co.nz</div>
    <div><svg width="14" height="14" viewBox="0 0 14 14"><circle cx="7" cy="7" r="6" fill="none" stroke="var(--blue)" stroke-width="1.5"/><path d="M1 7h12M7 1c-3 3-3 9 0 12M7 1c3 3 3 9 0 12" stroke="var(--blue)" stroke-width="1.2" fill="none"/></svg>www.kestrellineelectrical.co.nz</div>
  </div>

  <div class="abs phone">
    <svg width="20" height="20" viewBox="0 0 20 20"><circle cx="10" cy="10" r="9" fill="none" stroke="var(--white)" stroke-width="1.6"/><path d="M7 5l2 3-1.5 1.5a6 6 0 0 0 3 3L12 11l3 2-1.5 2C9 14.5 5.5 11 5 6.5z" fill="var(--white)"/></svg>
    +64 27 408 2197
  </div>
</main>
</body>
</html>
```